Business Cards & Stationary
Women's Religious Organization
Use same font as used in my logo
Open to fonts
Bright & Fun-filled
Dorinda L. Fennow
Chief Executive Officer
P.O.???
Linden Hollow, VA 20614
info@daisybloomz.example
www.daisybloomz.example
add twitter- @iamdaisybloomz
add facebook- DaisyBloomz
UPDATE: P.O. Box 6158 Captiol Heights, MD 20628
Ok here it is P.O. Box 6158
Capitol Heights, MD 20628-6158
Also, no waves please.
FYI: I prefer the round edges :-)
#1 I don't care to much for the designs all over can you send other?
#4 and #3can I see the other stationary with this set?
Designers, I need stationary as well.
Please check top right message box.
Hi, Please contact me for any questions. Looking for stationary and biz cards!

```html
<!DOCTYPE html>
<html lang="en">
<head>
<meta charset="utf-8">
<title>DaisyBloomz — Stationery Set</title>
<link rel="stylesheet" href="https://fonts.googleapis.com/css2?family=Cormorant+Garamond:wght@400;500&family=Cormorant+SC:wght@500&family=Didact+Gothic&display=swap">
<style>
  :root{
    --backdrop:#5e5e5e;
    --pink:#e2137b;
    --pink-light:#ee4f9a;
    --pink-deep:#b80f63;
    --ink:#222022;
    --ink-soft:#3a3839;
    --paper:#f7f7f9;
    --white:#ffffff;
    --grey-text:#444;
    --script:"Cormorant Garamond", Georgia, serif;
    --caps:"Cormorant SC", Georgia, serif;
    --tag:"Didact Gothic", Arial, sans-serif;
  }
  *{box-sizing:border-box;margin:0;padding:0}
  html,body{width:1200px;height:960px;overflow:hidden}
  body{background:var(--backdrop);position:relative;font-family:var(--caps);}

  .brand{font-family:var(--script);font-weight:400;letter-spacing:.5px;line-height:1;white-space:nowrap}
  .tagline{font-family:var(--tag);white-space:nowrap}

  /* Folder */
  .folder{position:absolute;left:60px;top:60px;width:340px;height:460px;
    background:linear-gradient(135deg,var(--pink-deep) 0%,var(--pink) 45%,var(--pink-light) 100%);
    display:flex;flex-direction:column;align-items:center;justify-content:center;gap:10px}
  .folder .brand{color:var(--white);font-size:44px}
  .folder .tagline{color:var(--white);font-size:14px}

  /* Letterhead */
  .letterhead{position:absolute;left:430px;top:60px;width:340px;height:440px;background:var(--paper)}
  .letterhead .logo{position:absolute;left:20px;top:30px}
  .letterhead .brand{color:var(--ink);font-size:22px}
  .letterhead .tagline{color:var(--ink);font-size:7px;margin-top:4px}
  .contact{position:absolute;border-left:1px solid var(--ink);padding-left:7px;color:var(--grey-text);font-size:8px;line-height:1.35}
  .contact .gap{height:8px}
  .contact .row{display:flex;align-items:center;gap:4px}
  .contact svg{width:7px;height:7px;fill:var(--pink);flex:none}
  .letterhead .contact{right:18px;top:22px}
  .url-tab{position:absolute;left:50%;transform:translateX(-50%);bottom:0;background:var(--pink);color:var(--white);
    font-family:var(--caps);letter-spacing:3px;font-size:8px;padding:6px 18px;border-radius:7px 7px 0 0;white-space:nowrap}

  /* Envelope */
  .envelope{position:absolute;left:800px;top:60px;width:360px;height:190px;background:var(--paper)}
  .envelope .logo{position:absolute;left:18px;top:20px}
  .envelope .brand{color:var(--ink);font-size:18px}
  .envelope .address{position:absolute;left:18px;top:52px;font-size:8px;color:var(--grey-text);line-height:1.35}

  /* Business cards */
  .card{position:absolute;width:350px;height:200px;border-radius:14px;overflow:hidden}
  .card-front{left:800px;top:280px;background:linear-gradient(160deg,var(--ink-soft),var(--ink))}
  .card-front .logo{position:absolute;left:22px;top:68px}
  .card-front .brand{color:var(--white);font-size:26px}
  .card-front .tagline{color:var(--white);font-size:7px;margin-top:5px}
  .card-front .contact{left:180px;top:28px;border-left:2px solid var(--pink);color:#ddd;font-size:8px}
  .card-front .person{font-family:var(--caps);color:var(--white);font-size:12px;letter-spacing:.5px}
  .card-front .role{font-size:6.5px;letter-spacing:.5px;color:#ccc}
  .card-back{left:800px;top:510px;background:var(--pink)}
  .card-back .brand{position:absolute;left:24px;top:58px;color:var(--white);font-size:34px}
  .social{position:absolute;left:24px;top:120px;display:flex;flex-direction:column;gap:7px;color:var(--white);font-size:10px;letter-spacing:1px}
  .social .row{display:flex;align-items:center;gap:7px}
  .social .dot{width:9px;height:9px;border-radius:2px;background:var(--white)}
  .card-back .url-tab{background:var(--white);color:var(--pink)}

  /* Cup */
  .cup{position:absolute;left:110px;top:580px;width:220px;height:320px}
  .cup .label{position:absolute;left:0;top:130px;width:220px;text-align:center}
  .cup .brand{color:var(--white);font-size:26px}
  .cup .tagline{color:var(--white);font-size:8px;margin-top:5px}

  /* Disc */
  .disc{position:absolute;left:440px;top:540px;width:360px;height:360px}
  .disc .label{position:absolute;left:0;top:62px;width:360px;text-align:center}
  .disc .brand{color:var(--white);font-size:30px}
  .disc .tagline{color:var(--white);font-size:8px;margin-top:5px}
</style>
</head>
<body>

  <section class="folder" aria-label="Presentation folder">
    <div class="brand">DaisyBloomz</div>
    <div class="tagline">Graceful | Grounded | Glowing</div>
  </section>

  <section class="letterhead" aria-label="Letterhead">
    <div class="logo">
      <div class="brand">DaisyBloomz</div>
      <div class="tagline">Graceful | Grounded | Glowing</div>
    </div>
    <div class="contact">
      <div>P.O.???</div>
      <div>Linden Hollow, VA 20614</div>
      <div class="gap"></div>
      <div class="row"><svg viewBox="0 0 10 10"><path d="M2 0h2l1 3-1.5 1a6 6 0 0 0 2.5 2.5L7 5l3 1v2c0 1-1 2-2 2A8 8 0 0 1 0 2c0-1 1-2 2-2z"/></svg>180.040.226.71</div>
      <div class="row"><svg viewBox="0 0 10 10"><path d="M2 0h2l1 3-1.5 1a6 6 0 0 0 2.5 2.5L7 5l3 1v2c0 1-1 2-2 2A8 8 0 0 1 0 2c0-1 1-2 2-2z"/></svg>301.555.014.2</div>
      <div class="row"><svg viewBox="0 0 10 10"><path d="M0 2h10v6H0z M0 2l5 3.5L10 2" fill="none" stroke="var(--pink)" stroke-width="1.2"/></svg>INFO@DAISYBLOOMZ.EXAMPLE</div>
    </div>
    <div class="url-tab">WWW.DAISYBLOOMZ.EXAMPLE</div>
  </section>

  <section class="envelope" aria-label="Envelope">
    <div class="logo"><div class="brand">DaisyBloomz</div></div>
    <div class="address">P.O.???<br>Linden Hollow, VA 20614</div>
    <div class="url-tab">WWW.DAISYBLOOMZ.EXAMPLE</div>
  </section>

  <section class="card card-front" aria-label="Business card front">
    <div class="logo">
      <div class="brand">DaisyBloomz</div>
      <div class="tagline">Graceful | Grounded | Glowing</div>
    </div>
    <div class="contact">
      <div class="person">Dorinda L. Fennow</div>
      <div class="role">CHIEF EXECUTIVE OFFICER</div>
      <div class="gap"></div>
      <div>P.O.???</div>
      <div>Linden Hollow, VA 20614</div>
      <div class="gap"></div>
      <div class="row"><svg viewBox="0 0 10 10"><path d="M2 0h2l1 3-1.5 1a6 6 0 0 0 2.5 2.5L7 5l3 1v2c0 1-1 2-2 2A8 8 0 0 1 0 2c0-1 1-2 2-2z"/></svg>180.040.226.71</div>
      <div class="row"><svg viewBox="0 0 10 10"><path d="M2 0h2l1 3-1.5 1a6 6 0 0 0 2.5 2.5L7 5l3 1v2c0 1-1 2-2 2A8 8 0 0 1 0 2c0-1 1-2 2-2z"/></svg>301.555.014.2</div>
      <div class="row"><svg viewBox="0 0 10 10"><path d="M0 2h10v6H0z M0 2l5 3.5L10 2" fill="none" stroke="var(--pink)" stroke-width="1.2"/></svg>INFO@DAISYBLOOMZ.EXAMPLE</div>
    </div>
    <div class="url-tab">WWW.DAISYBLOOMZ.EXAMPLE</div>
  </section>

  <section class="card card-back" aria-label="Business card back">
    <div class="brand">DaisyBloomz</div>
    <div class="social">
      <div class="row"><span class="dot"></span>@IAMDAISYBLOOMZ</div>
      <div class="row"><span class="dot"></span>DAISYBLOOMZ</div>
    </div>
    <div class="url-tab">WWW.DAISYBLOOMZ.EXAMPLE</div>
  </section>

  <section class="cup" aria-label="Branded cup">
    <svg width="220" height="320" viewBox="0 0 220 320">
      <path d="M10 0H210L185 320H35Z" fill="var(--pink)"/>
      <path d="M10 0H110L85 320H35Z" fill="var(--pink-light)" opacity=".35"/>
    </svg>
    <div class="label">
      <div class="brand">DaisyBloomz</div>
      <div class="tagline">Graceful | Grounded | Glowing</div>
    </div>
  </section>

  <section class="disc" aria-label="Branded disc">
    <svg width="360" height="360" viewBox="0 0 360 360">
      <circle cx="180" cy="180" r="178" fill="var(--pink)"/>
      <circle cx="180" cy="180" r="52" fill="#bfbfbf"/>
      <circle cx="180" cy="180" r="30" fill="var(--ink)"/>
    </svg>
    <div class="label">
      <div class="brand">DaisyBloomz</div>
      <div class="tagline">Graceful | Grounded | Glowing</div>
    </div>
  </section>

</body>
</html>
```